BRL Design Business Card

I need to develop a business card for my real estate design and investment company. Something clean, classic and professional with a modern vibe.

Industry/Entity Type

Real Estate

Font styles to use
Serif
Sans Serif

```html
<!DOCTYPE html>
<html lang="en">
<head>
<meta charset="UTF-8">
<title>BRL Design Business Card</title>
<link href="https://fonts.googleapis.com/css2?family=Open+Sans:wght@400;700&display=swap" rel="stylesheet">
<style>
  :root {
    --page-bg-top: #ffffff;
    --page-bg-bottom: #cfcfcf;
    --card-front: #221d1a;
    --card-back: #1b1b1b;
    --accent: #7a4a40;
    --text-muted: #5b5b5b;
    --text-soft: #4a4a4a;
  }
  * { margin: 0; padding: 0; box-sizing: border-box; }
  html, body { width: 1200px; height: 1200px; overflow: hidden; }
  body {
    background: radial-gradient(circle at 50% 30%, var(--page-bg-top) 0%, #ececec 55%, var(--page-bg-bottom) 100%);
    font-family: "Open Sans", Arial, sans-serif;
    display: flex;
    flex-direction: column;
    align-items: center;
    justify-content: center;
    gap: 60px;
  }
  .card {
    width: 770px;
    height: 440px;
    position: relative;
    box-shadow: 0 10px 30px rgba(0,0,0,0.18);
  }
  .card-front { background: var(--card-front); }
  .card-back { background: var(--card-back); }
  .brand-name {
    position: absolute;
    left: 50%;
    transform: translateX(-50%);
    color: var(--accent);
    font-weight: 400;
    font-size: 44px;
    letter-spacing: 4px;
    white-space: nowrap;
  }
  .card-front .brand-name { top: 180px; }
  .card-back .brand-name { top: 90px; font-size: 40px; }
  .holder {
    position: absolute;
    left: 40px;
    top: 230px;
  }
  .holder-name {
    color: var(--text-soft);
    font-weight: 700;
    font-size: 24px;
    letter-spacing: 1px;
  }
  .holder-role {
    color: var(--text-soft);
    font-size: 18px;
    margin-top: 2px;
  }
  .contact {
    position: absolute;
    display: flex;
    align-items: flex-start;
    gap: 12px;
    color: var(--text-muted);
    font-size: 17px;
    line-height: 1.3;
    white-space: nowrap;
  }
  .contact svg { flex: none; margin-top: 2px; }
  .contact-mobile { left: 40px; top: 310px; }
  .contact-phone { left: 300px; top: 345px; }
  .contact-address { left: 510px; top: 290px; }
  .contact-email { left: 510px; top: 380px; }
</style>
</head>
<body>
  <section class="card card-front" aria-label="Card front">
    <div class="brand-name">BRL Design</div>
  </section>

  <section class="card card-back" aria-label="Card back">
    <div class="brand-name">BRL Design</div>

    <div class="holder">
      <div class="holder-name">XXXXX XXXXX</div>
      <div class="holder-role">Director</div>
    </div>

    <div class="contact contact-mobile">
      <svg width="18" height="18" viewBox="0 0 18 18" aria-hidden="true">
        <rect x="1" y="1" width="16" height="16" rx="2" fill="var(--accent)"/>
        <rect x="6" y="3.5" width="6" height="11" rx="1" fill="none" stroke="#1b1b1b" stroke-width="1.4"/>
      </svg>
      <span>+00 (0) 000 000 000</span>
    </div>

    <div class="contact contact-phone">
      <svg width="18" height="18" viewBox="0 0 18 18" aria-hidden="true">
        <rect x="1" y="1" width="16" height="16" rx="2" fill="var(--accent)"/>
        <rect x="4" y="6" width="10" height="8" rx="1" fill="#1b1b1b"/>
        <rect x="5" y="3.5" width="8" height="2" fill="#1b1b1b"/>
      </svg>
      <span>+00 0 0000 0000</span>
    </div>

    <div class="contact contact-address">
      <svg width="18" height="18" viewBox="0 0 18 18" aria-hidden="true">
        <path d="M9 2 L16 8.5 H14 V16 H4 V8.5 H2 Z" fill="var(--accent)"/>
        <rect x="7.5" y="11" width="3" height="5" fill="#1b1b1b"/>
      </svg>
      <span>xxxxx, xxxxxxx xxx<br>18/5 xxxxxxx, xxxxx<br>xxxxx, xx,4200, Xxxxxx</span>
    </div>

    <div class="contact contact-email">
      <svg width="18" height="18" viewBox="0 0 18 18" aria-hidden="true">
        <rect x="1" y="1" width="16" height="16" rx="2" fill="var(--accent)"/>
        <rect x="3.5" y="5" width="11" height="8" fill="none" stroke="#1b1b1b" stroke-width="1.3"/>
        <path d="M3.5 5 L9 9.5 L14.5 5" fill="none" stroke="#1b1b1b" stroke-width="1.3"/>
      </svg>
      <span>xxxxxxxxxx@xxxxx.com</span>
    </div>
  </section>
</body>
</html>
```